Company Mission & Values Poster

I'd like an A2 Portrait Poster displaying our company's Mission & Values.
See our website for our logo, fonts, mission & values.
https://talvendo.com.au/

Our Mission: Creating homes for abundant life
Values: Love, Thinking, Team, Zoe.

Some ideas to consider:
Mission as the Headline then
A logo for each of the 4 Values and the words

Target Market(s)

Myself & my team

Industry/Entity Type

Real Estate

Font styles to use
Other font styles liked:
• Company fonts as seen on our website

```html
<!DOCTYPE html>
<html lang="en">
<head>
<meta charset="utf-8">
<title>Talvendo — Mission &amp; Values</title>
<link rel="stylesheet" href="https://fonts.googleapis.com/css2?family=Playfair+Display:wght@400;700;800&family=Great+Vibes&family=Inter:wght@400&family=Cormorant+Garamond:wght@500;600&display=swap">
<style>
  :root {
    --green: #063a2e;
    --cream: #f7f3e9;
    --cream-soft: #f4efe3;
    --line: #b9c0b6;
    --sketch-blue: #a9bfd3;
    --sketch-warm: #e8dfcf;
    --sketch-grey: #8c969a;
  }
  * { box-sizing: border-box; margin: 0; padding: 0; }
  html, body { width: 901px; height: 1200px; overflow: hidden; background: var(--cream); }
  .poster {
    position: relative;
    width: 901px;
    height: 1200px;
    background: var(--cream);
    color: var(--green);
    overflow: hidden;
  }
  .brand {
    position: absolute;
    top: 52px;
    left: 0;
    width: 100%;
    text-align: center;
    font-family: "Cormorant Garamond", serif;
    font-weight: 600;
    font-size: 70px;
    letter-spacing: 12px;
    line-height: 1;
  }
  .headline {
    position: absolute;
    top: 168px;
    left: 0;
    width: 100%;
    height: 90px;
  }
  .headline-script {
    position: absolute;
    left: 62px;
    top: -12px;
    font-family: "Great Vibes", cursive;
    font-size: 96px;
    line-height: 1;
    z-index: 2;
  }
  .headline-serif {
    position: absolute;
    left: 322px;
    top: 6px;
    font-family: "Playfair Display", serif;
    font-weight: 800;
    font-size: 66px;
    letter-spacing: -1px;
    line-height: 1;
  }
  .mission-band {
    position: absolute;
    top: 254px;
    left: 69px;
    width: 759px;
    height: 112px;
    background: var(--green);
    border-radius: 12px;
    color: var(--cream);
    display: flex;
    align-items: center;
    justify-content: center;
    font-family: "Playfair Display", serif;
    font-weight: 800;
    font-size: 80px;
    letter-spacing: -2px;
    line-height: 1;
  }
  .hero-art {
    position: absolute;
    top: 370px;
    left: 0;
    width: 901px;
    height: 470px;
    background:
      radial-gradient(ellipse 40% 45% at 45% 55%, rgba(140,160,180,0.55), transparent 70%),
      radial-gradient(ellipse 30% 30% at 60% 55%, rgba(232,190,140,0.45), transparent 70%),
      radial-gradient(ellipse 55% 55% at 50% 55%, var(--sketch-warm), transparent 80%),
      var(--cream);
  }
  .values {
    position: absolute;
    top: 838px;
    left: 52px;
    width: 797px;
    height: 250px;
    background: var(--cream-soft);
    border: 1px solid var(--line);
    border-radius: 14px;
    box-shadow: 0 8px 18px rgba(6,58,46,0.08);
    display: grid;
    grid-template-columns: 160px 242px 185px 210px;
    padding: 20px 0;
  }
  .value {
    display: flex;
    flex-direction: column;
    align-items: center;
    text-align: center;
    border-right: 1px solid var(--line);
  }
  .value:last-child { border-right: none; }
  .value-icon { width: 56px; height: 56px; margin-top: 8px; }
  .value-title {
    font-family: "Playfair Display", serif;
    font-weight: 400;
    font-size: 42px;
    letter-spacing: -1px;
    line-height: 1;
    margin-top: 8px;
  }
  .value-text {
    font-family: "Inter", sans-serif;
    font-size: 18.5px;
    letter-spacing: -0.4px;
    line-height: 24px;
    margin-top: 12px;
  }
  .footer {
    position: absolute;
    bottom: 0;
    left: 0;
    width: 100%;
    height: 80px;
    background: var(--green);
    color: var(--cream);
    display: flex;
    align-items: center;
    justify-content: center;
    gap: 18px;
  }
  .footer-cursor { width: 18px; height: 22px; }
  .footer-url {
    font-family: "Cormorant Garamond", serif;
    font-weight: 500;
    font-size: 46px;
    letter-spacing: 5px;
    line-height: 1;
  }
</style>
</head>
<body>
<main class="poster">
  <h1 class="brand">TALVENDO</h1>

  <div class="headline">
    <span class="headline-script">Creating</span>
    <span class="headline-serif">HOMES FOR</span>
  </div>
  <div class="mission-band">ABUNDANT LIFE</div>

  <div class="hero-art" role="img" aria-label="Watercolour and architectural sketch illustration of a modern two-storey home with large glass windows, a garden terrace and outdoor lounge, overlaid with blueprint lines and measurements"></div>

  <section class="values">
    <article class="value">
      <svg class="value-icon" viewBox="0 0 56 56" fill="none" stroke="currentColor" stroke-width="2.2" stroke-linecap="round" stroke-linejoin="round" aria-hidden="true">
        <path d="M28 24c-4-6-13-3-10 4 2 4 10 9 10 9s8-5 10-9c3-7-6-10-10-4z"/>
        <path d="M6 26v12l12 12v4M50 26v12L38 50v4"/>
        <path d="M6 30l10 10M50 30L40 40"/>
      </svg>
      <h2 class="value-title">Love</h2>
      <p class="value-text">Our love &amp;<br>respect for<br>people, those<br>we develop for</p>
    </article>
    <article class="value">
      <svg class="value-icon" viewBox="0 0 56 56" fill="none" stroke="currentColor" stroke-width="2.2" stroke-linecap="round" stroke-linejoin="round" aria-hidden="true">
        <path d="M22 30a12 12 0 1 1 12 0v6H22z"/>
        <path d="M23 41h10M25 46h6"/>
        <path d="M44 8l6 6-14 22-7 2 1-7z"/>
        <circle cx="44" cy="44" r="5"/>
      </svg>
      <h2 class="value-title">Thinking</h2>
      <p class="value-text">Our rigorous and<br>creative processes<br>create beautifully<br>considered solutions</p>
    </article>
    <article class="value">
      <svg class="value-icon" viewBox="0 0 56 56" fill="none" stroke="currentColor" stroke-width="2.2" stroke-linecap="round" stroke-linejoin="round" aria-hidden="true">
        <circle cx="28" cy="18" r="7"/>
        <circle cx="12" cy="22" r="5"/>
        <circle cx="44" cy="22" r="5"/>
        <path d="M14 44c0-9 6-14 14-14s14 5 14 14z"/>
        <path d="M3 40c0-7 4-10 9-10M53 40c0-7-4-10-9-10"/>
      </svg>
      <h2 class="value-title">Team</h2>
      <p class="value-text">We surround<br>ourselves with<br>best designers<br>and advisers</p>
    </article>
    <article class="value">
      <svg class="value-icon" viewBox="0 0 56 56" fill="none" stroke="currentColor" stroke-width="2.2" stroke-linecap="round" stroke-linejoin="round" aria-hidden="true">
        <circle cx="28" cy="28" r="9"/>
        <path d="M28 8v6M28 42v6M8 28h6M42 28h6M14 14l4 4M38 38l4 4M14 42l4-4M38 18l4-4"/>
      </svg>
      <h2 class="value-title">Zoe</h2>
      <p class="value-text">Creating places<br>for abundant life,<br>with exquisite<br>designs</p>
    </article>
  </section>

  <footer class="footer">
    <svg class="footer-cursor" viewBox="0 0 18 22" aria-hidden="true">
      <path d="M2 1l14 12H9l4 8-3 1-4-8-4 4z" fill="currentColor"/>
    </svg>
    <span class="footer-url">talvendo.com.au</span>
  </footer>
</main>
</body>
</html>
```